Portfolio site - Need a basic WordPress or SquareSpace site

I need a portfolio site where I have the option to keep updating it on my own. Therefore, I'm guessing I need one that uses WordPress or SquareSpace. I just need a simple and elegant design. I'm a writer (scholarly, fiction and journalism).

Target Market(s)

Adult

Industry/Entity Type

Writer

Number of Pages Required

4 page

Font styles to use
Serif

Colors
b7a5cd
e667a6
85abd2

Requirements
Must have
• Easily updatable features. I'll have to publish links and small blurbs from time to time. And maybe the occasional image.
• Pages should be:
• Home
• Work
• Press
• Contact

```html
<!DOCTYPE html>
<html lang="en">
<head>
<meta charset="utf-8">
<title>Marisol Averly — Writer</title>
<link rel="stylesheet" href="https://fonts.googleapis.com/css2?family=Rosarivo:ital@0;1&display=swap">
<style>
  :root {
    --lavender: #b7a5cd;
    --pink: #e667a6;
    --blue: #85abd2;
    --ink: #1a1a1a;
    --text: #333333;
    --grey: #555555;
    --white: #ffffff;
    --photo-dark: #2b2a30;
    --photo-light: #d9dbe0;
  }
  * { box-sizing: border-box; margin: 0; padding: 0; }
  html, body { width: 800px; height: 1200px; overflow: hidden; background: var(--white); }
  .page { position: relative; width: 800px; height: 1200px; font-family: "Rosarivo", Georgia, serif; color: var(--text); }

  .site-header { position: absolute; top: 0; left: 0; width: 800px; height: 103px; }
  .brand { position: absolute; left: 20px; top: 42px; font-family: "Rosarivo", Georgia, serif; font-size: 20px; line-height: 1; font-weight: 400; color: var(--ink); }
  .main-nav { position: absolute; left: 409px; top: 39px; display: flex; }
  .main-nav a { display: block; height: 30px; line-height: 30px; padding: 0 12px; font-size: 15px; color: var(--grey); text-decoration: none; }
  .main-nav a.is-active { background: var(--pink); color: var(--white); border-radius: 3px; padding: 0 13px; }

  .feature { position: absolute; left: 0; width: 800px; display: flex; }
  .feature-quote { background: var(--lavender); position: relative; }
  .feature-quote blockquote { position: absolute; font-size: 19px; line-height: 24px; color: var(--ink); }
  .feature-quote cite { display: block; font-size: 15px; font-style: italic; margin-top: 4px; }
  .photo { height: 100%; }

  .hero { top: 103px; height: 257px; }
  .hero .feature-quote { width: 402px; }
  .hero blockquote { left: 36px; top: 145px; width: 340px; }
  .hero .photo { width: 398px; background: linear-gradient(150deg, var(--photo-dark) 0%, #3e3c44 45%, var(--photo-light) 75%, #b8bac2 100%); }

  .news { position: absolute; top: 400px; left: 0; width: 800px; }
  .news-heading { text-align: center; font-size: 24px; font-style: italic; font-weight: 400; color: var(--pink); margin-top: 28px; }
  .news-item { position: absolute; top: 88px; width: 204px; }
  .news-rule { position: relative; height: 30px; }
  .news-rule::before { content: ""; position: absolute; left: 0; right: 0; top: 14px; height: 2px; background: var(--blue); }
  .news-badge { position: absolute; left: 50%; top: 0; width: 30px; height: 30px; margin-left: -15px; border-radius: 50%; background: var(--blue); }
  .news-title { font-size: 16px; font-weight: 400; color: var(--grey); margin-top: 26px; }
  .news-body { font-family: Arial, Helvetica, sans-serif; font-size: 11.5px; line-height: 14.4px; color: var(--ink); margin-top: 18px; }
  .news-more { display: block; font-family: Arial, Helvetica, sans-serif; font-size: 11.5px; line-height: 14.4px; color: var(--pink); text-decoration: none; }

  .studio { top: 771px; height: 287px; }
  .studio .photo { width: 400px; margin-left: 2px; background: linear-gradient(160deg, #e4e5e6 0%, #cfd1d2 40%, #e9532f 55%, #c9ccce 80%, #dcdedf 100%); }
  .studio .feature-quote { width: 398px; }
  .studio blockquote { left: 24px; top: 170px; width: 350px; }

  .site-footer { position: absolute; top: 1058px; left: 0; width: 800px; height: 142px; background: var(--blue); }
  .footer-brand { position: absolute; left: 26px; top: 65px; font-family: "Rosarivo", Georgia, serif; font-size: 15px; font-weight: 400; color: var(--white); }
  .copyright { position: absolute; left: 209px; top: 70px; font-size: 10px; color: var(--ink); }
  .social { position: absolute; left: 589px; top: 59px; display: flex; gap: 15px; list-style: none; }
  .social li { width: 22px; height: 22px; border-radius: 50%; background: var(--ink); }
</style>
</head>
<body>
<div class="page">
  <header class="site-header">
    <div class="brand">Marisol Averly</div>
    <nav class="main-nav">
      <a class="is-active" href="#">HOME</a>
      <a href="#">WORK</a>
      <a href="#">PRESS</a>
      <a href="#">CONTACT</a>
    </nav>
  </header>

  <section class="feature hero">
    <div class="feature-quote">
      <blockquote>To produce a mighty book, you must choose a mighty theme.<cite>– Harlan Merrow</cite></blockquote>
    </div>
    <div class="photo" role="img" aria-label="Close-up photo of a hand writing with a pen in a spiral notebook"></div>
  </section>

  <section class="news">
    <h2 class="news-heading">WHAT’S NEW?</h2>
    <article class="news-item" style="left:37px">
      <div class="news-rule"><svg class="news-badge" viewBox="0 0 30 30"><text x="15" y="24" text-anchor="middle" font-family="Georgia, serif" font-size="22" font-weight="700" fill="#fff">”</text></svg></div>
      <h3 class="news-title" style="margin-left:-2px">TITLE 1</h3>
      <p class="news-body" style="margin-left:-2px">Lorem ipsum dolor sit amet, consectetur adipiscing elit, sed do eiusmod tempor incididunt ut labore et dolore magna aliqua. Ut enim ad minim veniam, quis nostrud exercitation ullamco laboris nisi ut aliquip ex ea commodo consequat.<a class="news-more" href="#">READ MORE</a></p>
    </article>
    <article class="news-item" style="left:298px">
      <div class="news-rule"><svg class="news-badge" viewBox="0 0 30 30"><text x="15" y="24" text-anchor="middle" font-family="Georgia, serif" font-size="22" font-weight="700" fill="#fff">”</text></svg></div>
      <h3 class="news-title">TITLE 2</h3>
      <p class="news-body" style="margin-left:-5px">Duis aute irure dolor in reprehenderit in voluptate velit esse cillum dolore eu fugiat nulla pariatur. Excepteur sint occaecat cupidatat non proident, sunt in culpa qui officia deserunt mollit anim id est laborum.<a class="news-more" href="#">READ MORE</a></p>
    </article>
    <article class="news-item" style="left:558px">
      <div class="news-rule"><svg class="news-badge" viewBox="0 0 30 30"><text x="15" y="24" text-anchor="middle" font-family="Georgia, serif" font-size="22" font-weight="700" fill="#fff">”</text></svg></div>
      <h3 class="news-title">TITLE 3</h3>
      <p class="news-body">Sed ut perspiciatis unde omnis iste natus error sit voluptatem accusantium doloremque laudantium, totam rem aperiam, eaque ipsa quae ab illo inventore veritatis et quasi architecto beatae vitae dicta sunt explicabo.<a class="news-more" href="#">READ MORE</a></p>
    </article>
  </section>

  <section class="feature studio">
    <div class="photo" role="img" aria-label="Top-down photo of hands typing on a red typewriter beside a cup of coffee on a white wooden desk"></div>
    <div class="feature-quote">
      <blockquote>“We are all apprentices in a craft where no one ever becomes a master.”<cite>—Edgar Hollins</cite></blockquote>
    </div>
  </section>

  <footer class="site-footer">
    <div class="footer-brand">Marisol Averly</div>
    <p class="copyright">Copyright 2018. All Rights Reserved.</p>
    <ul class="social" aria-label="Social links">
      <li></li><li></li><li></li><li></li><li></li>
    </ul>
  </footer>
</div>
</body>
</html>
```